Kettle Pine Society - A Monthly Subscription Coffee Club - Shopify Website Design

A monthly subscription company. Need a Shopify Website Design and uploaded to fully work with Tidewell Renewals.

Please look at these sites for examples as well as the images I enclosed.

https://www.sipvaultory.com/
https://crumbcrate.com/
https://www.platewindly.com/
https://www.globalnibblers.com/

Number of Pages Required

1 page

```html
<!DOCTYPE html>
<html lang="en">
<head>
<meta charset="utf-8">
<title>Kettle Pine Society — Monthly Subscription Coffee Club</title>
<link href="https://fonts.googleapis.com/css2?family=Oswald:wght@500;600;700&family=Open+Sans:wght@400;600;700&display=swap" rel="stylesheet">
<style>
:root{
  --orange:#e8702a;
  --ink:#1b1b1b;
  --dark:#16110d;
  --footer:#121212;
  --cream:#fbf6ef;
  --grey:#f3f3f3;
  --muted:#777;
  --price:#2b6cb0;
  --white:#fff;
}
*{box-sizing:border-box;margin:0;padding:0}
html,body{width:1200px;height:4748px;overflow:hidden}
body{font-family:"Open Sans",Arial,sans-serif;color:var(--ink);background:var(--white);position:relative}
.abs{position:absolute}

/* header + hero */
.hero{position:absolute;left:0;top:0;width:1200px;height:800px;
  background:radial-gradient(ellipse at 50% 70%,#7a4a26 0%,#3a2414 35%,#120c08 75%);}
.site-header{position:absolute;left:0;top:0;width:1200px;height:120px;display:flex;align-items:center;padding:0 144px 0 110px}
.brand{font-family:"Open Sans",sans-serif;font-weight:600;font-size:24px;color:var(--white)}
.main-nav{display:flex;gap:26px;margin-left:auto;margin-right:40px}
.main-nav a{font-family:"Oswald",sans-serif;font-weight:500;font-size:17px;color:var(--white);text-decoration:none;letter-spacing:.5px}
.main-nav a.active{color:var(--orange)}
.header-icons{display:flex;gap:22px}
.hero-copy{position:absolute;left:0;top:300px;width:1200px;text-align:center;color:var(--white)}
.hero-copy h1{font-family:"Oswald",sans-serif;font-weight:700;font-size:52px;letter-spacing:2px}
.hero-copy p{font-size:19px;margin-top:6px}
.btn{display:inline-block;background:var(--orange);color:var(--white);font-family:"Oswald",sans-serif;font-weight:500;font-size:16px;padding:12px 28px;letter-spacing:1px}
.hero-copy .btn{margin-top:22px}
.hero-cup{position:absolute;left:380px;top:470px;width:440px;height:330px;border-radius:8px 8px 0 0;
  background:linear-gradient(180deg,#5b3318,#c89a62 60%,#e0c08f)}
.slider-arrow{position:absolute;top:384px;width:32px;height:32px;background:var(--white);display:flex;align-items:center;justify-content:center}
.dots{position:absolute;top:744px;left:0;width:1200px;display:flex;justify-content:center;gap:10px}
.dots span{width:14px;height:14px;border-radius:50%;border:2px solid #fff;opacity:.7}
.dots span:first-child{background:#fff}

/* features */
.features{position:absolute;top:800px;left:0;width:1200px;height:180px;background:var(--cream);display:flex;justify-content:center;gap:190px;align-items:center}
.feature{text-align:center;font-family:"Oswald",sans-serif;font-weight:500;font-size:19px;letter-spacing:.5px}
.feature svg{display:block;margin:0 auto 10px}

/* box grid */
.box-tile{position:absolute;width:448px;display:flex;flex-direction:column;align-items:center;justify-content:center;color:var(--white)}
.box-tile small{font-family:"Oswald",sans-serif;font-size:14px;letter-spacing:1px}
.box-tile strong{font-family:"Oswald",sans-serif;font-weight:600;font-size:22px;letter-spacing:1px;margin-top:4px}
.box-tile .btn{margin-top:12px;font-size:14px;padding:8px 18px}

/* sections */
.section-title{position:absolute;left:0;width:1200px;text-align:center}
.section-title h2{font-family:"Oswald",sans-serif;font-weight:600;font-size:40px;letter-spacing:1px;line-height:1.2}
.section-title p{font-size:18px;color:#444;margin-top:4px}
.product{position:absolute;width:200px;text-align:center}
.product .shot{height:260px;background:var(--grey);display:flex;align-items:center;justify-content:center;position:relative;overflow:hidden}
.product .pack{width:110px;height:170px;border-radius:6px}
.product .price{color:var(--price);font-weight:700;font-size:16px;margin-top:26px}
.product .name{font-size:15px;line-height:1.3;margin-top:4px}
.product .stars{color:var(--orange);font-size:15px;letter-spacing:2px;margin-top:6px}
.ribbon{position:absolute;top:16px;left:-30px;width:120px;background:var(--orange);color:#fff;font-size:12px;font-weight:700;transform:rotate(-45deg);text-align:center;padding:3px 0}

/* banner */
.inside-banner{position:absolute;top:2752px;left:0;width:1200px;height:496px;overflow:hidden;
  background:linear-gradient(90deg,#1a100a 0%,#2b1a10 45%,#3a2417 100%)}
.inside-copy{position:absolute;left:232px;top:96px;color:var(--white);z-index:1}
.inside-copy .brand{font-size:26px;color:var(--orange)}
.inside-copy h2{font-family:"Open Sans",sans-serif;font-weight:700;font-size:46px;line-height:1.18;margin-top:22px}

/* newsletter */
.newsletter{position:absolute;top:3936px;left:0;width:1200px;height:292px;background:linear-gradient(90deg,#2c1c12,#1d1712 40%,#171717)}
.newsletter h2{position:absolute;left:144px;top:96px;font-family:"Open Sans",sans-serif;font-weight:700;font-size:34px;line-height:1.2;color:var(--white)}
.newsletter p{position:absolute;left:144px;top:144px;font-size:13px;color:#ddd}
.newsletter .field{position:absolute;left:548px;top:122px;width:372px;height:50px;background:var(--white);padding:15px 18px;font-size:14px;color:#999}
.newsletter .btn{position:absolute;left:936px;top:122px;width:120px;height:50px;text-align:center;padding:14px 0}

/* footer */
.site-footer{position:absolute;top:4228px;left:0;width:1200px;height:520px;background:var(--footer);color:#ddd}
.footer-col{position:absolute;top:86px}
.footer-col h3{font-family:"Oswald",sans-serif;font-weight:600;font-size:20px;color:var(--white);letter-spacing:.5px}
.footer-col h3::after{content:"";display:block;width:34px;height:3px;background:var(--orange);margin-top:8px}
.footer-col ul{list-style:none;margin-top:18px}
.footer-col li{font-size:14px;line-height:27px}
.contact li{display:flex;gap:10px;align-items:flex-start;line-height:20px;margin-bottom:14px}
.footer-bottom{position:absolute;top:388px;left:144px;width:912px;border-top:1px solid #2c2c2c;padding-top:34px;display:flex;align-items:center;justify-content:space-between;font-size:14px}
.socials,.cards{display:flex;gap:10px}
.socials span{width:26px;height:26px;border-radius:50%;border:1.5px solid #bbb}
.cards span{width:38px;height:24px;border-radius:3px;background:#e8e8e8}
</style>
</head>
<body>

<section class="hero">
  <div class="hero-cup" role="img" aria-label="Photo of coffee beans pouring into a paper cup"></div>
  <header class="site-header">
    <div class="brand">Kettle Pine Society</div>
    <nav class="main-nav">
      <a class="active" href="#">HOME</a><a href="#">OUR BOXES</a><a href="#">ACCESSORIES</a><a href="#">SHOP</a><a href="#">CONTACT</a>
    </nav>
    <div class="header-icons">
      <svg width="24" height="24" viewBox="0 0 24 24" fill="none" stroke="#fff" stroke-width="2.4"><circle cx="10" cy="10" r="7"/><path d="M15 15l6 6"/></svg>
      <svg width="24" height="24" viewBox="0 0 24 24" fill="none" stroke="#fff" stroke-width="2"><circle cx="12" cy="8" r="4.5"/><path d="M3 22c1-5 5-7 9-7s8 2 9 7"/></svg>
      <svg width="26" height="24" viewBox="0 0 26 24" fill="none" stroke="#fff" stroke-width="2"><path d="M1 2h4l3 13h13l3-9H7"/><circle cx="10" cy="20" r="2"/><circle cx="19" cy="20" r="2"/></svg>
    </div>
  </header>
  <div class="hero-copy">
    <h1>KETTLE PINE SOCIETY</h1>
    <p>25% Off Your First Box With Code: OCT455</p>
    <span class="btn">GET YOUR BOX</span>
  </div>
  <div class="slider-arrow" style="left:32px"><svg width="12" height="14" viewBox="0 0 12 14"><path d="M9 1L3 7l6 6" stroke="#333" stroke-width="2.4" fill="none"/></svg></div>
  <div class="slider-arrow" style="right:32px"><svg width="12" height="14" viewBox="0 0 12 14"><path d="M3 1l6 6-6 6" stroke="#333" stroke-width="2.4" fill="none"/></svg></div>
  <div class="dots"><span></span><span></span><span></span></div>
</section>

<section class="features">
  <div class="feature">
    <svg width="70" height="52" viewBox="0 0 70 52" fill="none" stroke="#222" stroke-width="2.4"><path d="M4 8h38v30H4zM42 18h14l9 10v10H42z"/><circle cx="16" cy="42" r="6" fill="#fbf6ef"/><circle cx="54" cy="42" r="6" fill="#fbf6ef"/></svg>
    FREE SHIPPING
  </div>
  <div class="feature">
    <svg width="60" height="56" viewBox="0 0 60 56" fill="none" stroke="#222" stroke-width="2.4"><rect x="6" y="20" width="48" height="12"/><rect x="10" y="32" width="40" height="20"/><path d="M30 20v32M30 20c-6-14-18-10-12-2M30 20c6-14 18-10 12-2"/></svg>
    BEST SELLING COFFEE GIFTS
  </div>
  <div class="feature">
    <svg width="56" height="56" viewBox="0 0 56 56" fill="none" stroke="#222" stroke-width="2.4"><circle cx="28" cy="22" r="17"/><path d="M20 22l6 6 10-11M18 36l-6 16 8-4 4 7 4-11M38 36l6 16-8-4-4 7-4-11"/></svg>
    10 YEAR WARRANTY
  </div>
</section>

<div class="box-tile" style="left:144px;top:1028px;height:304px;background:linear-gradient(135deg,#3a2618,#8a5a34 55%,#2a1a10)" role="img" aria-label="Photo of a latte with coffee beans">
  <small>MONTH'S BOX</small><strong>NEMO VOLUPTATEM</strong><span class="btn">SHOP NOW</span>
</div>
<div class="box-tile" style="left:608px;top:1028px;height:304px;background:linear-gradient(135deg,#5a2a1e,#a0442e 45%,#3c5a2a)" role="img" aria-label="Photo of coffee cherries and a cup">
  <small>MONTH'S BOX</small><strong>NEMO VOLUPTATEM</strong>
</div>
<div class="box-tile" style="left:144px;top:1348px;height:312px;background:linear-gradient(135deg,#4a3a30,#9a7a62 50%,#2a2420)" role="img" aria-label="Photo of friends sharing coffee at a table">
  <small>MONTH'S BOX</small><strong>NEMO VOLUPTATEM</strong>
</div>
<div class="box-tile" style="left:608px;top:1348px;height:312px;background:radial-gradient(ellipse at 50% 60%,#7a4a26,#24160c 70%)" role="img" aria-label="Photo of beans splashing from a coffee cup">
  <small>MONTH'S BOX</small><strong>NEMO VOLUPTATEM</strong>
</div>

<div class="section-title" style="top:1720px"><h2>BEST SELLERS</h2><p>Monthly Subscription Coffee Club</p></div>

<div class="product" style="left:144px;top:1852px"><div class="shot" role="img" aria-label="Photo of black and white coffee pouches"><div class="pack" style="background:linear-gradient(90deg,#222 50%,#e4e4e4 50%)"></div></div><div class="price">$52.73</div><div class="name">Nemo enim ipsam<br>voluptatem quia voluptas</div><div class="stars">★★★★★</div></div>
<div class="product" style="left:376px;top:1852px"><div class="shot" role="img" aria-label="Photo of an instant coffee jar"><div class="ribbon">NEW</div><div class="pack" style="background:linear-gradient(180deg,#333,#4a2a18)"></div></div><div class="price">$52.73</div><div class="name">Nemo enim ipsam<br>voluptatem quia voluptas</div><div class="stars">★★★★★</div></div>
<div class="product" style="left:608px;top:1852px"><div class="shot" role="img" aria-label="Photo of a yellow coffee tin"><div class="pack" style="background:linear-gradient(180deg,#f2d43a,#e8c21a)"></div></div><div class="price">$52.73</div><div class="name">Nemo enim ipsam<br>voluptatem quia voluptas</div><div class="stars">★★★★★</div></div>
<div class="product" style="left:840px;top:1852px"><div class="shot" role="img" aria-label="Photo of a brown paper coffee cup"><div class="pack" style="background:linear-gradient(180deg,#3a2418,#6a3e22)"></div></div><div class="price">$52.73</div><div class="name">Nemo enim ipsam<br>voluptatem quia voluptas</div><div class="stars">★★★★★</div></div>

<div class="product" style="left:144px;top:2272px"><div class="shot" role="img" aria-label="Photo of black and white coffee pouches"><div class="pack" style="background:linear-gradient(90deg,#222 50%,#e4e4e4 50%)"></div></div><div class="price">$52.73</div><div class="name">Nemo enim ipsam<br>voluptatem quia voluptas</div><div class="stars">★★★★★</div></div>
<div class="product" style="left:376px;top:2272px"><div class="shot" role="img" aria-label="Photo of an instant coffee jar"><div class="pack" style="background:linear-gradient(180deg,#333,#4a2a18)"></div></div><div class="price">$52.73</div><div class="name">Nemo enim ipsam<br>voluptatem quia voluptas</div><div class="stars">★★★★★</div></div>
<div class="product" style="left:608px;top:2272px"><div class="shot" role="img" aria-label="Photo of a yellow coffee tin"><div class="pack" style="background:linear-gradient(180deg,#f2d43a,#e8c21a)"></div></div><div class="price">$52.73</div><div class="name">Nemo enim ipsam<br>voluptatem quia voluptas</div><div class="stars">★★★★★</div></div>
<div class="product" style="left:840px;top:2272px"><div class="shot" role="img" aria-label="Photo of a brown paper coffee cup"><div class="pack" style="background:linear-gradient(180deg,#3a2418,#6a3e22)"></div></div><div class="price">$52.73</div><div class="name">Nemo enim ipsam<br>voluptatem quia voluptas</div><div class="stars">★★★★★</div></div>

<section class="inside-banner">
  <div class="abs" style="left:0;top:0;width:220px;height:496px;background:linear-gradient(90deg,#5a3a22,rgba(42,26,16,0))" role="img" aria-label="Photo of coffee beans and a cup"></div>
  <div class="inside-copy">
    <div class="brand">Kettle Pine Society</div>
    <h2>What's Inside<br>the Box Each<br>Week</h2>
  </div>
  <div class="abs" style="left:620px;top:40px;width:520px;height:420px;background:linear-gradient(160deg,#6a4a34,#d9d4cc 55%,#f4f2ee)" role="img" aria-label="Photo of an open gift box with three coffee bags"></div>
</section>

<div class="section-title" style="top:3330px"><h2>SPECIAL PRODUCTS</h2><p>Monthly Subscription Coffee Club</p></div>

<div class="product" style="left:144px;top:3460px"><div class="shot" role="img" aria-label="Photo of a kraft coffee bag with beans" style="background:linear-gradient(180deg,#c49a66,#7a4e2a)"></div><div class="price">$52.73</div><div class="name">Nemo enim ipsam<br>voluptatem quia voluptas</div><div class="stars">★★★★★</div></div>
<div class="product" style="left:376px;top:3460px"><div class="shot" role="img" aria-label="Photo of paper coffee bags" style="background:linear-gradient(180deg,#e8e2d8,#a88a66)"></div><div class="price">$52.73</div><div class="name">Nemo enim ipsam<br>voluptatem quia voluptas</div><div class="stars">★★★★★</div></div>
<div class="product" style="left:608px;top:3460px"><div class="shot" role="img" aria-label="Photo of black coffee canisters" style="background:linear-gradient(180deg,#d8d8d8,#2a2a2a)"></div><div class="price">$52.73</div><div class="name">Nemo enim ipsam<br>voluptatem quia voluptas</div><div class="stars">★★★★★</div></div>
<div class="product" style="left:840px;top:3460px"><div class="shot" role="img" aria-label="Photo of stacked coffee sacks" style="background:linear-gradient(180deg,#4a2a1e,#8a3a2a)"></div><div class="price">$52.73</div><div class="name">Nemo enim ipsam<br>voluptatem quia voluptas</div><div class="stars">★★★★★</div></div>

<section class="newsletter">
  <div class="abs" style="left:0;top:0;width:440px;height:292px;background:radial-gradient(ellipse at 30% 70%,#6a4226,rgba(40,26,18,0) 70%)" role="img" aria-label="Photo of a scoop of roasted coffee beans"></div>
  <h2>Join our Newsletter</h2>
  <p>Enter your email and subscribe to receive updates</p>
  <div class="field">Enter your E - mail</div>
  <span class="btn">SUBSCRIBE</span>
</section>

<footer class="site-footer">
  <div class="footer-col" style="left:144px"><h3>QUICK LINKS</h3><ul><li>Home</li><li>About Us</li><li>Privacy Policy</li><li>Shipping &amp; Returns</li><li>Contact Us</li><li>Sitemap</li></ul></div>
  <div class="footer-col" style="left:340px"><h3>CATEGORIES</h3><ul><li>Sed ut perspiciatis</li><li>Unde omnis iste natus</li><li>Voluptatem accusantium</li><li>Doloremque laudantium</li><li>Totam rem aperiam</li></ul></div>
  <div class="footer-col" style="left:568px"><h3>OUR BRANDS</h3><ul><li>Sed ut perspiciatis</li><li>Unde omnis iste natus</li><li>Voluptatem accusantium</li><li>Doloremque laudantium</li><li>Totam rem aperiam</li></ul></div>
  <div class="footer-col contact" style="left:784px"><h3>CONTACT US</h3><ul>
    <li><svg width="14" height="18" viewBox="0 0 14 18"><path d="M7 1a6 6 0 00-6 6c0 5 6 10 6 10s6-5 6-10a6 6 0 00-6-6z" fill="#ddd"/><circle cx="7" cy="7" r="2" fill="#121212"/></svg><span>Kettle Pine Society<br>125 Larch Street, Suite 4<br>Portland, OR 97201</span></li>
    <li><svg width="14" height="14" viewBox="0 0 14 14"><path d="M3 1l3 3-2 2c1 2 2 3 4 4l2-2 3 3-2 2C6 13 1 8 1 3z" fill="#ddd"/></svg><span>Phone: 555-0142-7788</span></li>
    <li><svg width="14" height="12" viewBox="0 0 14 12" fill="none" stroke="#ddd" stroke-width="1.5"><rect x="1" y="1" width="12" height="10"/><path d="M1 1l6 5 6-5"/></svg><span>E-mail: info@kettlepinesociety.com</span></li>
    <li><svg width="14" height="14" viewBox="0 0 14 14" fill="none" stroke="#ddd" stroke-width="1.5"><circle cx="7" cy="7" r="6"/><path d="M7 3v4h3"/></svg><span>Open time: 9AM to 5PM</span></li>
  </ul></div>
  <div class="footer-bottom">
    <span>© 2020 Kettle Pine Society. All Rights Reserved.</span>
    <div class="socials"><span></span><span></span><span></span><span></span><span></span><span></span></div>
    <div class="cards"><span></span><span></span><span></span></div>
  </div>
</footer>

</body>
</html>
```